The Lantern Assembly Pitchdeck Template

The Lantern Assembly would like a branded pitch deck template design for members to use when presenting their projects and proposals. The deck should include 10-15 different slide designs, each with the same branded theme, but with a variety of icon graphics and other design features that will empower members to easily create a beautiful pitch deck just by adding written content.

Please visit thelantern.org to get a sense for our branding - purple, space, galaxy, white font and the planetary logo are some commonalities.

Here are 2 google drive links with some additional designs

https://files.cloudnestbox.net/share/u/1/dir/8KpqZr3Tn5Yb-wLxVd2Hc-Qm4jEsAf7Ug

https://files.cloudnestbox.net/share/u/1/dir/6Rtb2-Lm9Xc4-hNwq813Fvkzpe_Jd7Sa

```html
<!DOCTYPE html>
<html lang="en">
<head>
<meta charset="utf-8">
<title>The Lantern Assembly – Pitch Deck Template</title>
<link rel="stylesheet" href="https://fonts.googleapis.com/css2?family=Montserrat:wght@700;800&family=Roboto:wght@400;500;700&display=swap">
<style>
  :root {
    --canvas: #a6a7a9;
    --ink: #ffffff;
    --ink-soft: #e4e2ee;
    --orange: #ff6a0c;
    --night: #131316;
    --cell: #1b1b1e;
  }
  * { box-sizing: border-box; margin: 0; padding: 0; }
  html, body { width: 1200px; height: 3916px; overflow: hidden; }
  body { background: var(--canvas); font-family: "Roboto", Arial, sans-serif; color: var(--ink); position: relative; }

  .slide { position: absolute; width: 981px; height: 552px; overflow: hidden; box-shadow: 0 2px 6px rgba(0,0,0,.25); }
  .slide--cover    { left: 114px; top: 113px; }
  .slide--about    { left: 114px; top: 741px; }
  .slide--vision   { left: 114px; top: 1367px; }
  .slide--intent   { left: 105px; top: 1997px; }
  .slide--partners { left: 114px; top: 2624px; }
  .slide--support  { left: 110px; top: 3253px; }

  .abs { position: absolute; }
  .photo { position: absolute; }

  /* Cover */
  .slide--cover { background: radial-gradient(ellipse at 25% 50%, #3a1f6e 0%, #1a1650 45%, #0f0d33 100%); }
  .cover__art { left: 0; top: 0; width: 490px; height: 552px;
    background: radial-gradient(ellipse 40% 14% at 50% 50%, rgba(255,150,220,.75), rgba(120,40,140,.35) 60%, transparent 100%); }
  .cover__divider { left: 491px; top: 55px; width: 1px; height: 440px; background: rgba(255,255,255,.25); }
  .cover__title { left: 550px; top: 108px; font-family: "Montserrat", Arial, sans-serif; font-weight: 800; font-size: 48px; letter-spacing: 1px; line-height: 1.1; }
  .cover__tag { left: 553px; top: 178px; color: var(--orange); font-weight: 700; font-size: 15px; }
  .cover__date { left: 553px; top: 220px; font-weight: 700; font-size: 12px; }
  .cover__brand { left: 553px; top: 310px; display: flex; align-items: center; gap: 18px; font-weight: 700; font-size: 30px; letter-spacing: 3px; }
  .cover__brand-dot { width: 48px; height: 48px; border-radius: 50%; background: var(--ink); }
  .cover__button { left: 546px; top: 450px; width: 227px; height: 41px; border-radius: 21px; background: var(--orange);
    display: flex; align-items: center; justify-content: center; font-weight: 700; font-size: 13px; }

  /* About */
  .slide--about { background: radial-gradient(ellipse at 60% 55%, #5a3f80 0%, #2d2258 40%, #14112e 100%); }
  .about__art { left: 32px; top: 130px; width: 450px; height: 293px; border-radius: 50%;
    background: radial-gradient(ellipse at 55% 45%, #d9924a 0%, #8a4a22 45%, rgba(40,20,20,.85) 75%, transparent 100%); }
  .about__copy { left: 558px; top: 135px; width: 360px; }
  .heading-xl { font-weight: 500; font-size: 34px; letter-spacing: .5px; line-height: 1.2; margin-bottom: 18px; }
  .body-copy { font-size: 11.8px; line-height: 21.5px; text-align: justify; color: var(--ink-soft); margin-bottom: 14px; }

  /* Shared dark slides */
  .slide--dark { background: var(--night); }
  .slide__title { position: absolute; left: 61px; top: 22px; font-weight: 700; font-size: 34px; letter-spacing: .5px;
    line-height: 44px; padding-left: 26px; }
  .slide__title::before { content: ""; position: absolute; left: 0; top: 7px; width: 7px; height: 30px; background: var(--ink); }
  .brand-mark { position: absolute; right: 63px; top: 30px; display: flex; align-items: center; gap: 8px;
    font-weight: 700; font-size: 24px; letter-spacing: 5px; line-height: 1; }
  .brand-mark__dot { width: 14px; height: 14px; border-radius: 50%; background: var(--ink); }

  .grid-cell { position: absolute; width: 277px; height: 172px; }
  .text-cell { background: var(--cell); display: flex; flex-direction: column; align-items: center; justify-content: center;
    text-align: center; padding: 0 22px; }
  .text-cell h3 { font-weight: 500; font-size: 17px; margin-bottom: 10px; }
  .text-cell p { font-size: 11.5px; line-height: 20px; color: var(--ink-soft); }

  /* Intentions */
  .intent__copy { left: 62px; top: 62px; width: 361px; }
  .intent__copy .heading-xl { font-weight: 700; margin-bottom: 22px; }
  .intent__copy .body-copy { font-size: 12.4px; line-height: 21.5px; }
  .intent__art { left: 490px; top: 0; width: 491px; height: 552px;
    background: radial-gradient(ellipse 45% 35% at 50% 38%, #d63fa0 0%, #6a2fa0 45%, #1d1b4a 80%),
                linear-gradient(180deg, #121233 0%, #1d1b4a 70%, #e0a040 92%, #1a1410 100%);
    background-blend-mode: screen; }

  /* Partners */
  .slide--partners { background: radial-gradient(ellipse at 70% 40%, #2c2540 0%, #16131f 70%, #0e0c14 100%); }
  .partners__art { left: 0; top: 0; }
  .partners__title { left: 59px; top: 105px; font-weight: 700; font-size: 30px; }
  .partner { position: absolute; }
  .partner__badge { position: absolute; width: 78px; height: 78px; border-radius: 50%; border: 4px solid #0c0c10; }
  .partner h4 { font-weight: 500; font-size: 17px; line-height: 20px; margin-bottom: 8px; }
  .partner p { font-size: 11.5px; line-height: 18px; color: var(--ink-soft); width: 440px; }

  /* Support */
  .support__col { position: absolute; top: 334px; width: 275px; text-align: center; padding: 0 6px; }
  .support__col h3 { font-weight: 500; font-size: 17px; margin-bottom: 10px; }
  .support__col p { font-size: 11.3px; line-height: 19.6px; color: var(--ink-soft); }
</style>
</head>
<body>

<section class="slide slide--cover">
  <div class="photo cover__art" role="img" aria-label="Glowing pink and violet black hole against a starfield"></div>
  <div class="abs cover__divider"></div>
  <h1 class="abs cover__title">THE LANTERN</h1>
  <p class="abs cover__tag">UNITING HUMANITY AS ONE</p>
  <p class="abs cover__date">April, 2020</p>
  <div class="abs cover__brand"><span class="cover__brand-dot"></span>LANTERN</div>
  <div class="abs cover__button">PRESENTATION NAME</div>
</section>

<section class="slide slide--about">
  <div class="photo about__art" role="img" aria-label="Fiery amber ringed planet with a lone figure standing on its ring, set in a starry nebula"></div>
  <div class="abs about__copy">
    <h2 class="heading-xl">WHO ARE WE</h2>
    <p class="body-copy">The Lantern Assembly is a spiritual, conscious and regenerative non-profit organisation established for furthering the upliftment, enlightenment, spiritual realisation, and general welfare of people throughout the world, the betterment of life on planet Earth, and other spiritual, environmental, humanitarian, and beneficent purpose.</p>
    <p class="body-copy">Buddhism, Christianity, Hinduism, Islam, Judaism and other religions are belief systems. The Lantern exists whether you believe in it or not.</p>
  </div>
</section>

<section class="slide slide--dark slide--vision">
  <h2 class="slide__title">WHAT WE ENVISION</h2>
  <div class="brand-mark"><span class="brand-mark__dot"></span>LUMA</div>

  <div class="grid-cell" style="left:61px;top:131px;background:linear-gradient(160deg,#0d2a55,#2aa0d8 45%,#101c30 80%,#3a3a40);" role="img" aria-label="Blue spiral galaxy over a desert with a lone figure"></div>
  <div class="grid-cell text-cell" style="left:353px;top:131px;">
    <h3>PLANET</h3>
    <p>A World that lives in harmony with Nature; restore and protect Mother Earth, including the Animal Kingdom.</p>
  </div>
  <div class="grid-cell" style="left:643px;top:131px;background:linear-gradient(180deg,#6a2c4a,#e05a4a 50%,#3a1a2a 75%,#1a1218);" role="img" aria-label="Ringed planet rising over a red sunset landscape"></div>

  <div class="grid-cell text-cell" style="left:61px;top:307px;">
    <h3>PEOPLE</h3>
    <p>A World that meets the needs of every human being as a birth right, providing the foundation for self-actualisation.</p>
  </div>
  <div class="grid-cell" style="left:353px;top:307px;background:linear-gradient(180deg,#05070c,#2a4a7a 30%,#c8d4e0 60%,#6a7080);" role="img" aria-label="Person seen from behind looking down on Earth's clouds from orbit"></div>
  <div class="grid-cell text-cell" style="left:643px;top:307px;">
    <h3>PEACE</h3>
    <p>A World that chooses peace, love and harmony, awake and aware of its connection with everything.</p>
  </div>
</section>

<section class="slide slide--dark slide--intent">
  <div class="abs intent__copy">
    <h2 class="heading-xl">INTENTIONS</h2>
    <p class="body-copy">The Lantern Assembly, members, missionaries, stewards, sponsors, partners, and donors are working on various initiatives to fulfil our intentions. As a collective we are focusing on every area; from education, healthcare, economics, finance, governance &amp; technology, to space travel, art, music and transformational experiences.</p>
    <p class="body-copy">Our mission is to protect the Spirit of Air, Water, Land and Food; to create a system that supports the people and the planet; to redistribute wealth; protect human rights; serve justice and implement the conscious economy. We are focused on building a global community, transforming local environments, integration with Indigenous tribes and the reformation of society. We are interested in new paradigm schools and Universities, incubators for regenerative technology, natural medicine, empowering micro-industries, entrepreneurs, investors, inventors, artists and creatives.</p>
  </div>
  <div class="photo intent__art" role="img" aria-label="Magenta and blue nebula cloud shaped like a tree above a figure on a hill at dusk"></div>
</section>

<section class="slide slide--partners">
  <svg class="abs partners__art" width="360" height="552" viewBox="0 0 360 552" role="img" aria-label="Purple spiral galaxy above Earth with a figure standing on a rocky peak">
    <defs>
      <linearGradient id="partnersSky" x1="0" y1="0" x2="0" y2="1">
        <stop offset="0" stop-color="#3a2a8a"/>
        <stop offset=".45" stop-color="#a070d8"/>
        <stop offset=".75" stop-color="#3a5ab0"/>
        <stop offset="1" stop-color="#1a1620"/>
      </linearGradient>
    </defs>
    <path d="M0 0 H210 Q400 276 210 552 H0 Z" fill="url(#partnersSky)"/>
    <path d="M210 0 Q400 276 210 552" fill="none" stroke="#ffffff" stroke-width="9"/>
  </svg>
  <h2 class="abs partners__title">PARTNERS</h2>

  <div class="partner__badge" style="left:333px;top:31px;background:radial-gradient(circle,#5a3a9a,#1c1840);"></div>
  <div class="partner" style="left:433px;top:34px;">
    <h4>LUMEN CIRCLE</h4>
    <p>Lumen Circle is a group of organisations that belong to The Lantern, and meet the standards defined by the Assembly of what it means to be</p>
  </div>

  <div class="partner__badge" style="left:368px;top:133px;background:#1c1c20;"></div>
  <div class="partner" style="left:470px;top:137px;">
    <h4>SPROUTLINE</h4>
    <p>Sproutline is a payment platform and financial ecosystem to empower humanity and heal our planet. Crafted from systems that reflect the latest in financial,</p>
  </div>

  <div class="partner__badge" style="left:394px;top:239px;background:#141414;"></div>
  <div class="partner" style="left:494px;top:233px;">
    <h4>KINDRED HANDS</h4>
    <p style="width:430px;">Kindred Hands is a high level network of game changers that are not only dominating in their field, but who are also dedicated to extending human life on Earth for as long as possible.</p>
  </div>

  <div class="partner__badge" style="left:370px;top:341px;background:#1e5a78;"></div>
  <div class="partner" style="left:471px;top:341px;">
    <h4>RESONANT FIELD NETWORK</h4>
    <p>Resonant Field Network is an immersive experiential network of Yoga, Meditation, Mindfulness, Virtual Reality (VR), Online Learning, Digital Music, Personal</p>
  </div>

  <div class="partner__badge" style="left:333px;top:441px;background:#ffffff;"></div>
  <div class="partner" style="left:433px;top:444px;">
    <h4>MYCELO</h4>
    <p>Mycelo build dapps and tools to facilitate humanity's transition to a globally regenerative and thriving civilization</p>
  </div>
</section>

<section class="slide slide--dark slide--support">
  <h2 class="slide__title">SUPPORT THE MINISTRY</h2>
  <div class="brand-mark"><span class="brand-mark__dot"></span>LUMA</div>

  <div class="photo" style="left:61px;top:118px;width:275px;height:174px;background:linear-gradient(180deg,#2a2a5a,#8a6aa0 55%,#2a1a2a 80%,#120c14);" role="img" aria-label="Planets in orbit rings above a dark mountain range"></div>
  <div class="photo" style="left:351px;top:118px;width:276px;height:174px;background:radial-gradient(ellipse at 50% 40%,#e07ae0,#6a2a9a 45%,#1a1030 80%);" role="img" aria-label="Glowing purple star over violet sand dunes"></div>
  <div class="photo" style="left:642px;top:118px;width:275px;height:174px;background:radial-gradient(ellipse 55% 25% at 50% 50%,#e0e6ff,#3a4ab0 45%,#0d1040 90%);" role="img" aria-label="Black hole with bright accretion disk in deep blue space"></div>

  <div class="support__col" style="left:61px;">
    <h3>PARTNER</h3>
    <p>We are stronger together. If you are a conscious and regenerative project or organisation doing good in the world, please apply to join the Assembly now, and benefit from a network of resources, knowledge and expertise including funding, technical support, legal, tax and accounting, marketing, operational expense</p>
  </div>
  <div class="support__col" style="left:351px;">
    <h3>CONTRIBUTE</h3>
    <p>Take action by contributing your time, love and energy. Explore the Assembly, its projects, and all partner organisations in the DHO, a Decentralised Human Organisation. Discover paid roles, quests, and opportunities available across the globe within our ever expanding community.</p>
  </div>
  <div class="support__col" style="left:642px;">
    <h3>MEMBERSHIP</h3>
    <p>The Law of Personal Return states that giving is receiving! In accordance with this Universal Law, The Assembly gives back to its Members. Tax-deductible donations are used to fund Conscious and regenerative projects and organisations that create a positive impact on the people and the planet, as well as wealth for</p>
  </div>
</section>

</body>
</html>
```